Harrowgate Financial Coaching LLC - Needed clean black business card

Business card for personal financial coaching practice located on Las Vegas NV, new startup. Back of card needs to have "how it works" to match the website.

Font styles to use
Sans Serif

Colors

Designer to choose colors to be used in the design.

```html
<!DOCTYPE html>
<html lang="en">
<head>
<meta charset="utf-8">
<title>Harrowgate Financial Coaching LLC – Business Card</title>
<link href="https://fonts.googleapis.com/css2?family=Montserrat:wght@600;700&family=Questrial&display=swap" rel="stylesheet">
<style>
  :root {
    --backdrop: #2a2a2a;
    --card: #0d0d0d;
    --ink: #f4f4f4;
    --ink-soft: #e2e2e2;
  }
  * { margin: 0; padding: 0; box-sizing: border-box; }
  html, body {
    width: 1200px; height: 1200px; overflow: hidden;
    background: var(--backdrop);
  }
  .sheet {
    width: 1200px; height: 1200px;
    display: flex; flex-direction: column;
    align-items: center; justify-content: center; gap: 44px;
  }
  .card {
    width: 900px; height: 514px;
    background: var(--card);
    color: var(--ink);
    font-family: "Questrial", "Century Gothic", sans-serif;
    position: relative;
  }
  /* Back side */
  .card--back { padding: 118px 70px 0 70px; }
  .how-title {
    font-family: "Montserrat", sans-serif;
    font-weight: 700; font-size: 23px; letter-spacing: 0.2px;
    margin-bottom: 10px;
  }
  .how-list { list-style: none; }
  .how-list li {
    font-size: 19.5px; line-height: 31px; color: var(--ink-soft);
    padding-left: 30px; position: relative; white-space: nowrap;
  }
  .how-list li::before {
    content: ""; position: absolute; left: 0; top: 12px;
    width: 8px; height: 8px; border-radius: 50%; background: var(--ink);
  }
  /* Front side */
  .card--front { padding: 98px 62px 0 0; text-align: right; }
  .company {
    font-family: "Montserrat", sans-serif;
    font-weight: 700; font-size: 30px; letter-spacing: 1.5px;
    text-transform: uppercase;
  }
  .contact { position: absolute; right: 62px; top: 300px; }
  .person { font-size: 31px; letter-spacing: 0.8px; margin-bottom: 4px; }
  .contact-line {
    font-size: 21px; line-height: 36px; color: var(--ink-soft);
    display: flex; justify-content: flex-end; align-items: center; gap: 16px;
  }
  .contact-line.plain { padding-right: 0; }
  .contact-line .icon { width: 22px; height: 22px; flex: none; }
  .spacer { display: inline-block; width: 22px; }
</style>
</head>
<body>
<main class="sheet">

  <section class="card card--back" aria-label="Card back">
    <h2 class="how-title">How It Works</h2>
    <ul class="how-list">
      <li>All free one-time consultations are in-person meetings only.</li>
      <li>Paid appointments may be scheduled for in-person or virtual meetings.</li>
      <li>Select the session, date and time that works best for your schedule.</li>
      <li>Start your journey of financial freedom at harrowgatefinancialcoaching.com</li>
    </ul>
  </section>

  <section class="card card--front" aria-label="Card front">
    <h1 class="company">Harrowgate Financial Coaching LLC</h1>
    <div class="contact">
      <p class="person">Dale Merriton</p>
      <p class="contact-line">Dale@harrowgatefinancialcoaching.com<span class="spacer"></span></p>
      <p class="contact-line">702-555-0148
        <svg class="icon" viewBox="0 0 24 24" aria-hidden="true"><path fill="#f4f4f4" d="M6.6 10.8a15.1 15.1 0 0 0 6.6 6.6l2.2-2.2a1 1 0 0 1 1-.25 11.4 11.4 0 0 0 3.6.57 1 1 0 0 1 1 1V20a1 1 0 0 1-1 1A17 17 0 0 1 3 4a1 1 0 0 1 1-1h3.5a1 1 0 0 1 1 1c0 1.25.2 2.45.57 3.57a1 1 0 0 1-.25 1z"/></svg>
      </p>
      <p class="contact-line">4120 W Sunset Crest Rd #105-B, Las Vegas, NV 89147
        <svg class="icon" viewBox="0 0 24 24" aria-hidden="true"><rect x="2" y="5" width="20" height="14" fill="#f4f4f4"/><path d="M2 5l10 8 10-8M2 19l7.5-7M22 19l-7.5-7" stroke="#0d0d0d" stroke-width="1.6" fill="none"/></svg>
      </p>
      <p class="contact-line">harrowgatefinancialcoaching.com
        <svg class="icon" viewBox="0 0 24 24" aria-hidden="true"><g fill="none" stroke="#f4f4f4" stroke-width="1.6"><circle cx="12" cy="12" r="9.5"/><ellipse cx="12" cy="12" rx="4.2" ry="9.5"/><path d="M2.5 12h19M4 7h16M4 17h16"/></g></svg>
      </p>
    </div>
  </section>

</main>
</body>
</html>
```